Web Design for Harbor vNet

Need a website for 24/7 online Tv station. Looking for something unique, fresh and different.

When you click on site, I want viewers to automatically see video player. Video player should take up about 70% screen. Still need sections to show thumbnail clicks of our mission - Inspire, Inform and Entertain. Also need section to highlight new shows or events.

This is a family based TV station that will feature Christian content, news, per pay view movies, music videos, sermons from churches. I want site to appeal to 18 -40 year demo graphic. Even though based in California, I also want site appealing enough to all cultures worldwide.

Go to Streamly and search our channel (harborvnet) for some footages and logo.

Also visit www.harborvnet-demo.com to see logo. Need a design that matches logo.

Updates as of 8/28/13:-

http://video.kindhandsaid-demo.org/channel/animals-agriculture/
KHTV – like the look and feel. Left side to have 16:9 screen with player and on the right will be still pictures slide show

http://www.zuvwatch-demo.com/?camp=XoX512&tracking_ID=000000&K_CLICKID=00000000-0000-0000-0000-000000000000#home/
ZUV – I like the 16:9 screen (I don’t want mine too big – about 60% of screen)
I want a black background that will also match Harbor vNet red and white logo (see uploaded file)
Updates

KHTV – like the look and feel.  Left side to have 16:9 screen with player and on the right will be still pictures slide show

 

Reason: Need more time for poll results to come in and narrow down to one or two designs.

Target Market(s)

zPhone, zTab generation

I like the look and feel Kind Hands Aid TV

Industry/Entity Type

Tv

```html
<!DOCTYPE html>
<html lang="en">
<head>
<meta charset="utf-8">
<title>Harbor vNet</title>
<link rel="stylesheet" href="https://fonts.googleapis.com/css2?family=Open+Sans:wght@400;600;700&display=swap">
<style>
:root{
  --red:#e0262b;
  --dark:#2b2b2b;
  --band:#333333;
  --blue-deep:#165a85;
  --amber:#f58a32;
  --coral:#e9505b;
  --sky:#2a78aa;
  --white:#ffffff;
}
*{box-sizing:border-box;margin:0;padding:0}
html,body{width:788px;height:1200px;overflow:hidden}
body{position:relative;background:var(--dark);font-family:"Open Sans",Arial,sans-serif;color:var(--white)}
.abs{position:absolute}
.topline{left:0;top:0;width:788px;height:4px;background:var(--red)}
.header{left:0;top:4px;width:788px;height:75px;background:var(--dark)}
.brand{left:64px;top:20px;display:flex;align-items:center;gap:8px;font-size:34px;font-weight:700;letter-spacing:-1px;color:var(--white)}
.brand-dot{width:14px;height:14px;background:var(--red)}
.search{left:551px;top:31px;width:177px;height:39px;background:#444;padding:5px}
.search-inner{display:flex;height:29px;background:var(--red);padding:3px}
.search-field{flex:1;background:var(--white);font-size:9px;font-style:italic;color:#777;padding:6px 8px}
.search-btn{width:26px;display:flex;align-items:center;justify-content:center}
.nav{left:0;top:80px;width:788px;height:32px;background:linear-gradient(#6a6a6a,#3c3c3c);font-size:11px;text-transform:uppercase}
.nav a{color:var(--white);text-decoration:none;display:block;line-height:32px;position:absolute}
.nav .active{background:var(--red);left:63px;width:72px;text-align:center}
.stage{left:0;top:112px;width:788px;height:319px;background:#000}
.stage-side{left:66px;top:112px;width:611px;height:319px;background:#161616}
.stage-inner{left:106px;top:112px;width:572px;height:319px;background:#1d1d1d}
.player{left:138px;top:135px;width:510px;height:277px;background:#000}
.play{left:369px;top:233px}
.progress{left:138px;top:386px;width:510px;height:5px;background:var(--red)}
.controls{left:138px;top:391px;width:510px;height:21px;background:linear-gradient(#3a3a3a,#222);display:flex;align-items:center;font-size:8px;color:#ddd}
.mission{left:0;top:431px;width:788px;height:66px;background:var(--band);border-top:1px solid #444}
.mission-icons{left:63px;top:431px;width:183px;height:66px;background:#2a2a2a}
.tile{top:440px;width:49px;height:49px;display:flex;align-items:center;justify-content:center}
.mission-title{left:302px;top:446px;font-size:16px;font-weight:400}
.mission-text{left:304px;top:470px;font-size:9.5px;color:#ddd}
.btn{left:609px;top:452px;width:100px;height:27px;background:linear-gradient(#3a7ea6,#2b6688);border-radius:3px;font-size:12px;text-align:center;line-height:27px;color:#dfeef7;text-decoration:none}
.row{left:0;width:788px}
.row-inspire{top:497px;height:175px;background:linear-gradient(180deg,#2b80b2,var(--blue-deep))}
.row-inform{top:672px;height:165px;background:var(--band);border-top:1px solid #444}
.row-entertain{top:837px;height:173px;background:linear-gradient(180deg,#f28c3a,#ec7a26)}
.row-head{display:flex;align-items:center;gap:6px;font-size:15px;text-transform:uppercase}
.row-badge{width:22px;height:22px;display:flex;align-items:center;justify-content:center}
.thumb{width:198px;height:81px;border:2px solid var(--white)}
.thumb-a{background:linear-gradient(90deg,#0d0d0d 40%,#3a2a24 75%,#151515)}
.thumb-b{background:linear-gradient(135deg,#c9a58a,#b95a45 45%,#7e8a4a 75%,#e8e6e0)}
.thumb-c{background:linear-gradient(90deg,#e39b7a,#b99a86 40%,#5a3b44 70%,#d9d2c9)}
.film{position:absolute;left:0;bottom:0;width:24px;height:24px;display:flex;align-items:center;justify-content:center}
.caption{font-size:12px;width:220px}
.arrow{font-size:20px;color:var(--white)}
.footer{left:0;top:1010px;width:788px;height:190px;background:#2d2d2d}
.col-title{font-size:13px;text-transform:uppercase;display:flex;align-items:center;gap:8px}
.col-text{font-size:8.5px;line-height:13px;color:#e6e6e6}
.divider{width:1px;background:#4a4a4a}
.email{left:506px;top:1083px;width:126px;height:20px;background:var(--white);border-radius:3px;font-size:8.5px;font-style:italic;color:#666;padding:4px 9px}
.rule{left:66px;top:1122px;width:650px;height:1px;background:#4a4a4a}
.foot-brand{left:72px;top:1140px;display:flex;align-items:center;gap:6px;font-size:22px;font-weight:700;color:var(--white)}
.legal{left:75px;top:1181px;font-size:8.5px;color:#eee}
.social{top:1138px;width:25px;height:25px;background:#8e8e8e}
</style>
</head>
<body>
<div class="abs topline"></div>
<header class="abs header"></header>
<div class="abs brand"><span>Harbor vNet</span><span class="brand-dot"></span></div>
<div class="abs search"><div class="search-inner"><div class="search-field">Search...</div>
<div class="search-btn"><svg width="13" height="13" viewBox="0 0 13 13"><circle cx="5" cy="5" r="3.8" fill="none" stroke="#fff" stroke-width="1.8"/><line x1="8" y1="8" x2="12" y2="12" stroke="#fff" stroke-width="2"/></svg></div></div></div>

<nav class="abs nav">
  <a class="active" href="#">Home</a>
  <a href="#" style="left:157px">Programs</a>
  <a href="#" style="left:252px">Advertise</a>
  <a href="#" style="left:347px">About Us</a>
  <a href="#" style="left:437px">Subscribe</a>
  <a href="#" style="left:530px">Opportunities</a>
  <a href="#" style="left:653px">Contact Us</a>
</nav>

<section class="abs stage"></section>
<div class="abs stage-side"></div>
<div class="abs stage-inner"></div>
<div class="abs player"></div>
<svg class="abs play" width="54" height="54" viewBox="0 0 54 54"><circle cx="27" cy="27" r="25" fill="none" stroke="#aaa" stroke-width="2"/><path d="M21 16 L37 27 L21 38Z" fill="#aaa"/></svg>
<div class="abs progress"></div>
<div class="abs controls">
  <svg style="margin-left:20px" width="10" height="11" viewBox="0 0 10 11"><path d="M0 0 L10 5.5 L0 11Z" fill="#ccc"/></svg>
  <svg style="margin-left:20px" width="16" height="11" viewBox="0 0 16 11"><path d="M0 3.5H3L7 0V11L3 7.5H0Z" fill="#ccc"/><path d="M9.5 3 Q11.5 5.5 9.5 8 M11.5 1.5 Q15 5.5 11.5 9.5" stroke="#ccc" fill="none"/></svg>
  <span style="margin-left:10px;font-weight:700">0:00</span><span>&nbsp;/ 0:00</span>
  <span style="margin-left:auto;font-size:13px">+</span>
  <span style="margin-left:12px;color:#999">Streamly</span>
  <svg style="margin:0 10px" width="12" height="12" viewBox="0 0 12 12" stroke="#ccc" fill="none"><path d="M0 4V0H4M8 0H12V4M12 8V12H8M4 12H0V8"/></svg>
</div>

<section class="abs mission"></section>
<div class="abs mission-icons"></div>
<div class="abs tile" style="left:96px;background:var(--amber)"><svg width="30" height="30" viewBox="0 0 30 30" fill="none" stroke="#fff" stroke-width="1.8"><circle cx="15" cy="13" r="7"/><path d="M12 20v4h6v-4M15 2v3M4 13H1M29 13h-3M6 5l2 2M24 5l-2 2"/></svg></div>
<div class="abs tile" style="left:146px;background:var(--coral)"><svg width="32" height="32" viewBox="0 0 32 32"><circle cx="16" cy="16" r="14" fill="none" stroke="#fff" stroke-width="2"/><circle cx="17" cy="9" r="2" fill="#fff"/><path d="M14 14h4l-2 10h3" stroke="#fff" stroke-width="2.4" fill="none"/></svg></div>
<div class="abs tile" style="left:196px;background:var(--sky)"><svg width="30" height="30" viewBox="0 0 30 30" fill="#fff"><path d="M3 4 Q10 1 16 4 Q16 16 9.5 19 Q3 16 3 4Z"/><path d="M14 11 Q20 8 27 11 Q27 23 20.5 26 Q14 23 14 11Z" fill="#dbe9f3"/></svg></div>
<h2 class="abs mission-title">Our mission</h2>
<p class="abs mission-text">Our mission is to inspire, inform and entertain our viewers.</p>
<a class="abs btn" href="#">Contact us</a>

<section class="abs row row-inspire"></section>
<div class="abs row-head" style="left:71px;top:515px"><span class="row-badge" style="background:var(--amber)"><svg width="14" height="14" viewBox="0 0 14 14" fill="none" stroke="#fff" stroke-width="1.3"><circle cx="7" cy="7" r="3.5"/><path d="M7 0v2M7 12v2M0 7h2M12 7h2"/></svg></span>Inspire</div>
<div class="abs thumb thumb-a" style="left:70px;top:551px;border-color:var(--amber)" role="img" aria-label="Still of a host speaking to camera"><span class="film" style="background:var(--amber)"><svg width="12" height="10" viewBox="0 0 12 10"><rect x="0.5" y="0.5" width="11" height="9" fill="none" stroke="#fff"/><rect x="3" y="2.5" width="6" height="5" fill="#fff"/></svg></span></div>
<div class="abs thumb thumb-b" style="left:293px;top:549px" role="img" aria-label="Hands mixing a salad in a glass bowl"><span class="film" style="background:rgba(220,220,220,.85)"><svg width="12" height="10" viewBox="0 0 12 10"><rect x="0.5" y="0.5" width="11" height="9" fill="none" stroke="#333"/><rect x="3" y="2.5" width="6" height="5" fill="#333"/></svg></span></div>
<div class="abs thumb thumb-c" style="left:517px;top:549px" role="img" aria-label="People seated around a kitchen table"><span class="film" style="background:rgba(220,220,220,.85)"><svg width="12" height="10" viewBox="0 0 12 10"><rect x="0.5" y="0.5" width="11" height="9" fill="none" stroke="#333"/><rect x="3" y="2.5" width="6" height="5" fill="#333"/></svg></span></div>
<p class="abs caption" style="left:70px;top:637px">Savory Table's Corn Salsa</p>
<p class="abs caption" style="left:295px;top:639px">Caleb's Story (Full)</p>
<p class="abs caption" style="left:517px;top:636px">Savory Table's Hearty Chicken</p>
<span class="abs arrow" style="left:722px;top:572px">&rsaquo;</span>

<section class="abs row row-inform"></section>
<div class="abs row-head" style="left:71px;top:690px"><span class="row-badge" style="background:var(--coral);font-style:italic;font-weight:700;font-size:14px">i</span>Inform</div>
<div class="abs thumb thumb-a" style="left:70px;top:717px;border-color:var(--coral)" role="img" aria-label="Still of a host speaking to camera"><span class="film" style="background:var(--coral)"><svg width="12" height="10" viewBox="0 0 12 10"><rect x="0.5" y="0.5" width="11" height="9" fill="none" stroke="#fff"/><rect x="3" y="2.5" width="6" height="5" fill="#fff"/></svg></span></div>
<div class="abs thumb thumb-b" style="left:293px;top:716px" role="img" aria-label="Hands mixing a salad in a glass bowl"><span class="film" style="background:rgba(220,220,220,.85)"><svg width="12" height="10" viewBox="0 0 12 10"><rect x="0.5" y="0.5" width="11" height="9" fill="none" stroke="#333"/><rect x="3" y="2.5" width="6" height="5" fill="#333"/></svg></span></div>
<div class="abs thumb thumb-c" style="left:517px;top:716px" role="img" aria-label="People seated around a kitchen table"><span class="film" style="background:rgba(220,220,220,.85)"><svg width="12" height="10" viewBox="0 0 12 10"><rect x="0.5" y="0.5" width="11" height="9" fill="none" stroke="#333"/><rect x="3" y="2.5" width="6" height="5" fill="#333"/></svg></span></div>
<p class="abs caption" style="left:70px;top:803px">Savory Table's Corn Salsa</p>
<p class="abs caption" style="left:295px;top:804px">Caleb's Story (Full)</p>
<p class="abs caption" style="left:517px;top:802px">Savory Table's Hearty Chicken</p>
<span class="abs arrow" style="left:722px;top:740px">&rsaquo;</span>

<section class="abs row row-entertain"></section>
<div class="abs row-head" style="left:72px;top:855px"><span class="row-badge" style="background:var(--sky)"><svg width="14" height="14" viewBox="0 0 14 14" fill="#fff"><path d="M1 2 Q4 1 7 2 Q7 8 4 9 Q1 8 1 2Z"/><path d="M6 5 Q9 4 13 5 Q13 11 9.5 12 Q6 11 6 5Z" fill="#dbe9f3"/></svg></span>Entertain</div>
<div class="abs thumb thumb-a" style="left:70px;top:882px;border-color:var(--sky)" role="img" aria-label="Still of a host speaking to camera"><span class="film" style="background:var(--sky)"><svg width="12" height="10" viewBox="0 0 12 10"><rect x="0.5" y="0.5" width="11" height="9" fill="none" stroke="#fff"/><rect x="3" y="2.5" width="6" height="5" fill="#fff"/></svg></span></div>
<div class="abs thumb thumb-b" style="left:293px;top:880px" role="img" aria-label="Hands mixing a salad in a glass bowl"><span class="film" style="background:rgba(220,220,220,.85)"><svg width="12" height="10" viewBox="0 0 12 10"><rect x="0.5" y="0.5" width="11" height="9" fill="none" stroke="#333"/><rect x="3" y="2.5" width="6" height="5" fill="#333"/></svg></span></div>
<div class="abs thumb thumb-c" style="left:517px;top:880px" role="img" aria-label="People seated around a kitchen table"><span class="film" style="background:rgba(220,220,220,.85)"><svg width="12" height="10" viewBox="0 0 12 10"><rect x="0.5" y="0.5" width="11" height="9" fill="none" stroke="#333"/><rect x="3" y="2.5" width="6" height="5" fill="#333"/></svg></span></div>
<p class="abs caption" style="left:70px;top:968px;color:#fde3cf">Savory Table's Corn Salsa</p>
<p class="abs caption" style="left:295px;top:970px;color:#fde3cf">Caleb's Story (Full)</p>
<p class="abs caption" style="left:517px;top:967px;color:#fde3cf">Savory Table's Hearty Chicken</p>
<span class="abs arrow" style="left:722px;top:905px">&rsaquo;</span>

<footer class="abs footer"></footer>
<div class="abs col-title" style="left:68px;top:1020px"><svg width="14" height="12" viewBox="0 0 14 12"><path d="M1 3 L9 1 L13 4 L5 7Z" fill="#f0a24a"/><path d="M1 3 V7 L5 11 L13 8 V4 L5 7Z" fill="#d9782a"/></svg>Isa 40:31</div>
<p class="abs col-text" style="left:67px;top:1047px;width:190px">but those who hope in the LORD will renew their strength. They will soar on wings like eagles; they will run and not grow weary, they will walk and not be faint.</p>
<div class="abs divider" style="left:269px;top:1010px;height:105px"></div>
<div class="abs col-title" style="left:286px;top:1020px"><svg width="15" height="13" viewBox="0 0 15 13"><ellipse cx="6" cy="5" rx="6" ry="4.5" fill="#e9505b"/><ellipse cx="10" cy="8" rx="5" ry="4" fill="#c23a44"/></svg>New Shows &amp; Events</div>
<p class="abs col-text" style="left:288px;top:1047px;width:195px"><strong style="font-size:9.5px;color:#fff">Lorem ipsum dolor sit amet, conse.</strong><br>Proin aliquet, enim quis sagittis rutrum, purus metus posuere nibh, sit amet egestas dolor consectetur adipiscing elit....<span style="color:var(--red)">more</span></p>
<div class="abs divider" style="left:488px;top:1010px;height:105px"></div>
<div class="abs col-title" style="left:507px;top:1020px"><svg width="18" height="12" viewBox="0 0 18 12" fill="#4a8cc7"><circle cx="6" cy="3" r="3"/><path d="M0 12 Q0 6 6 6 Q12 6 12 12Z"/><circle cx="13" cy="3.5" r="2.5" opacity=".8"/><path d="M10 8 Q13 6 18 8 V12 H12Z" opacity=".8"/></svg>Keep in Touch</div>
<p class="abs col-text" style="left:508px;top:1047px;width:225px">Proin aliquet, enim quis sagittis rutrum, purus metus</p>
<p class="abs" style="left:508px;top:1066px;font-size:9px;font-weight:700">Sign up to our newsletter</p>
<div class="abs email">Email address<span style="position:absolute;right:8px;top:1px;font-style:normal;font-size:13px;color:#333">&rsaquo;</span></div>
<div class="abs rule"></div>
<div class="abs foot-brand"><span>Harbor vNet</span><span style="width:10px;height:10px;background:#8e8e8e"></span></div>
<p class="abs legal">Harbor vNet &nbsp;&copy; 2013 &nbsp;&nbsp; | &nbsp;&nbsp; Privacy Policy</p>
<div class="abs social" style="left:608px"></div>
<div class="abs social" style="left:635px;background:#3a3a3a"></div>
<div class="abs social" style="left:662px"></div>
<div class="abs social" style="left:689px"></div>
</body>
</html>
```